Business cards to launch an education platform

Hi,
I am looking at having new business cards designed.
I am a startup, developing a web platform for schools and university, the education world. It's an online assessment system.
I would like a card that looks classy, and that is using the colors and the font of my logo.

I have attached:
1) my logo
2) A business card that I have designed quickly so you can have all the information required in the card, but I really don't like it.
3) The font that I am using (Lato Regular) to design my web platform
4) Some screenshots of my web platform so you can have a look at the style that I have.

Target Market(s)

Major market: Education system: Schools and university
Minor markets: Business in general

Industry/Entity Type

Business

Contact Information for Business Card

Lydia Marsh
Director

M: 0437 681 902
E: lydia.marsh@copperLeafSystems.com.au

Requirements
Must have
• The colors of my logo

```html
<!DOCTYPE html>
<html lang="en">
<head>
<meta charset="utf-8">
<title>Copper Leaf Systems – Business Card</title>
<link href="https://fonts.googleapis.com/css2?family=Lato:wght@400;700&display=swap" rel="stylesheet">
<style>
  :root {
    --page-bg: #e9eaec;
    --card-white: #f6f7f8;
    --card-black: #0b0c0e;
    --brand-blue: #2a8fd0;
    --blue-light: #3fa6dd;
    --blue-deep: #1762b0;
    --ink-white: #ffffff;
    --edge-shadow: #101418;
  }
  * { margin: 0; padding: 0; box-sizing: border-box; }
  html, body {
    width: 1200px; height: 902px; overflow: hidden;
    background: var(--page-bg);
    font-family: "Lato", sans-serif;
  }
  .sheet {
    width: 1200px; height: 902px;
    display: flex; flex-direction: column;
    align-items: center; justify-content: center; gap: 56px;
  }
  .card {
    position: relative;
    width: 660px; height: 378px;
    border-radius: 4px; overflow: hidden;
    box-shadow: 0 10px 28px rgba(0,0,0,0.18);
  }
  .card-back {
    background: radial-gradient(ellipse at 45% 55%, #1a1d22 0%, var(--card-black) 70%);
  }
  .card-front { background: var(--card-white); }
  .card-art { position: absolute; inset: 0; width: 100%; height: 100%; }

  .brand {
    position: absolute;
    display: flex; align-items: center; gap: 18px;
    color: var(--brand-blue);
    font-weight: 400; letter-spacing: 2px;
  }
  .brand-mark {
    width: 58px; height: 58px;
    background: var(--brand-blue);
    border-radius: 3px;
  }
  .card-back .brand { left: 50%; top: 50%; transform: translate(-50%, -50%); font-size: 38px; }
  .card-front .brand { left: 150px; top: 78px; font-size: 34px; }
  .card-front .brand-mark { width: 52px; height: 52px; }

  .holder {
    position: absolute; left: 32px; bottom: 36px;
    color: var(--ink-white);
  }
  .holder-name { font-size: 32px; font-weight: 700; line-height: 1.05; }
  .holder-role { font-size: 20px; font-weight: 400; margin-top: 4px; }

  .divider {
    position: absolute; left: 262px; top: 232px;
    width: 1.5px; height: 108px;
    background: rgba(255,255,255,0.85);
  }
  .contact {
    position: absolute; left: 280px; top: 246px;
    list-style: none; color: var(--ink-white);
    font-size: 16px; line-height: 1;
  }
  .contact li { display: flex; align-items: center; gap: 9px; margin-bottom: 16px; }
  .contact svg { width: 18px; height: 18px; flex: none; }
</style>
</head>
<body>
<main class="sheet">

  <section class="card card-back" aria-label="Card back">
    <div class="brand">
      <span class="brand-mark"></span>
      <span class="brand-name">Copper Leaf Systems</span>
    </div>
  </section>

  <section class="card card-front" aria-label="Card front">
    <svg class="card-art" viewBox="0 0 660 378" preserveAspectRatio="none" aria-hidden="true">
      <defs>
        <linearGradient id="bandBlue" x1="0" y1="0" x2="1" y2="1">
          <stop offset="0" stop-color="#4eb2e4"/>
          <stop offset="0.55" stop-color="#2a8fd0"/>
          <stop offset="1" stop-color="#1762b0"/>
        </linearGradient>
      </defs>
      <path d="M0,206 L82,228 L580,160 L612,40 L660,40 L660,378 L0,378 Z" fill="url(#bandBlue)"/>
      <path d="M0,200 L82,222 L580,154 L608,40" fill="none" stroke="var(--edge-shadow)" stroke-width="7" stroke-linejoin="miter"/>
      <path d="M0,206 L82,228 L580,160 L612,40" fill="none" stroke="#ffffff" stroke-width="2"/>
    </svg>

    <div class="brand">
      <span class="brand-mark"></span>
      <span class="brand-name">Copper Leaf Systems</span>
    </div>

    <div class="holder">
      <p class="holder-name">Lydia Marsh</p>
      <p class="holder-role">Director</p>
    </div>

    <span class="divider"></span>

    <ul class="contact">
      <li>
        <svg viewBox="0 0 18 18" aria-hidden="true"><rect x="0.5" y="0.5" width="17" height="17" rx="2" fill="#fff"/><path d="M5 4.5c1-.6 1.8 1.4 1.4 2-.3.4-.8.5-.5 1.2.5 1.1 1.5 2.1 2.6 2.6.7.3.8-.2 1.2-.5.6-.4 2.6.4 2 1.4-.8 1.4-2.2 1.7-4 .6C5.9 10.7 4.4 9 3.8 7.3 3.4 6 4 5 5 4.5z" fill="#1f78c1"/></svg>
        <span>0437 681 902</span>
      </li>
      <li>
        <svg viewBox="0 0 18 18" aria-hidden="true"><rect x="0.5" y="3" width="17" height="12" rx="1.5" fill="#fff"/><path d="M1.5 4.5 L9 10 L16.5 4.5" fill="none" stroke="#1f78c1" stroke-width="1.4"/></svg>
        <span>lydia.marsh@copperLeafSystems.com.au</span>
      </li>
    </ul>
  </section>

</main>
</body>
</html>
```